| Pairlocket | ||
| "Lanternmade Insurance" (this tagline includes the mathmatic "squared" symbol-see logo #161 winner) | ||
| Use fonts in logo. However, we may provide other direction on fonts for Address/Phone Numbers, etc. | ||
Cutting-Edge Modern Bright & Fun-filled |
| Dana R. Whitlock, MBA | ||
| Agency Principal | ||
| To Be Determined | ||
| TBD | ||
| dana@trypairlocket.com | ||
| www.trypairlocket.com | ||
1. We will need business cards for 2 people, Dana Whitlock (info provided above) and Morgan Whitlock...info as follows: Morgan P. Whitlock, MBA Agency Principal morgan@trypairlocket.com cell: 555.204.7316 2. Designer has provided final files to Mark Studio Hive. #161 was selected as Winner. This design has multiple components, please note. 3. Our logo style and design is somewhat "Retro" and cool, hip. We are in the insurance industry but definitely want to achieve a different "non-standard" look and feel. 4. Read Logo Brief for more information about the style of the two (twin brothers) Agency Principals. |
We are thinking that the "bottle cap" portion of our logo along with the "Pairlocket" portion would look good on the back of the business card. The bottle cap portion taking up most of the back of the card. Would like various options for the back. |
Download project material |
| pairlocket_17707.pdf |
| 1_17708.ai |
| Oak_Cellar_Depot_Business_Card_1_17709.jpg Pairlocket - Bus Card - example card design. We would like to see a style similar to this. |
| Brisk_Kettle_Business_Card_Example_17710.jpg Pairlocket - Bus Card - example card design. We would like to see a style similar to this. |

```html
<!DOCTYPE html>
<html lang="en">
<head>
<meta charset="utf-8">
<title>Pairlocket Business Card</title>
<link href="https://fonts.googleapis.com/css2?family=Open+Sans:wght@400;600;700;800&display=swap" rel="stylesheet">
<style>
  :root {
    --backdrop: #e9e6e1;
    --card: #ffffff;
    --brand-green: #5f9e3e;
    --brand-blue: #1f5a8f;
    --ink: #3a3a3a;
    --ink-soft: #6b6b6b;
    --badge-ring: #8a8f94;
    --badge-face: #cfd6dc;
  }
  * { margin: 0; padding: 0; box-sizing: border-box; }
  html, body { width: 1200px; height: 541px; overflow: hidden; }
  body {
    background: var(--backdrop);
    font-family: "Open Sans", Arial, sans-serif;
    position: relative;
  }
  .card {
    position: absolute;
    top: 108px;
    width: 504px;
    height: 343px;
    background: var(--card);
    box-shadow: 0 3px 10px rgba(0,0,0,0.18);
    overflow: hidden;
  }
  .card--front { left: 72px; }
  .card--back { left: 605px; }

  /* Front */
  .brand {
    position: absolute;
    left: 28px;
    top: 60px;
    display: flex;
    align-items: center;
    gap: 10px;
  }
  .brand__dot {
    width: 30px; height: 30px;
    border-radius: 50%;
    background: var(--brand-green);
  }
  .brand__name {
    font-size: 30px;
    font-weight: 800;
    color: var(--brand-green);
    letter-spacing: -0.5px;
  }
  .tagline {
    position: absolute;
    left: 30px;
    top: 104px;
    font-size: 8.5px;
    font-weight: 700;
    letter-spacing: 1.4px;
    text-transform: uppercase;
    color: var(--ink-soft);
  }
  .contacts {
    position: absolute;
    left: 322px;
    top: 68px;
    list-style: none;
  }
  .contacts li {
    display: flex;
    align-items: center;
    gap: 9px;
    height: 17px;
    font-size: 11px;
    color: var(--ink);
  }
  .contacts svg { width: 11px; height: 11px; fill: var(--brand-green); flex: none; }
  .name-band {
    position: absolute;
    left: 0; top: 199px;
    width: 288px; height: 43px;
    background: var(--brand-blue);
    padding: 6px 0 0 28px;
    color: #fff;
  }
  .name-band__name { font-size: 14px; font-weight: 700; line-height: 17px; }
  .name-band__name small { font-size: 10px; font-weight: 400; }
  .name-band__role { font-size: 11px; line-height: 15px; padding-left: 60px; }
  .band-rule {
    position: absolute;
    left: 288px; top: 199px;
    width: 216px; height: 4px;
    background: var(--brand-blue);
  }
  .address {
    position: absolute;
    left: 322px; top: 210px;
    font-size: 11px;
    line-height: 16px;
    color: var(--ink);
  }
  .front-base {
    position: absolute;
    left: 0; bottom: 0;
    width: 100%; height: 8px;
    background: var(--brand-blue);
    opacity: 0.0;
  }

  /* Back */
  .badge {
    position: absolute;
    left: 192px; top: 70px;
    width: 120px; height: 120px;
  }
  .back-web {
    position: absolute;
    left: 0; top: 226px;
    width: 100%;
    text-align: center;
    font-size: 12px;
    color: var(--brand-green);
  }
</style>
</head>
<body>
  <section class="card card--front">
    <div class="brand">
      <span class="brand__dot"></span>
      <span class="brand__name">Pairlocket</span>
    </div>
    <p class="tagline">Lanternmade Insurance</p>

    <ul class="contacts">
      <li><svg viewBox="0 0 12 12"><path d="M3 1l2 2.5-1.2 1.2a7 7 0 0 0 3.5 3.5L8.5 7 11 9l-1.5 2A9 9 0 0 1 1 2.5z"/></svg>000.000.0000</li>
      <li><svg viewBox="0 0 12 12"><rect x="3" y="0.5" width="6" height="11" rx="1.2"/></svg>555.318.4420</li>
      <li><svg viewBox="0 0 12 12"><rect x="1" y="4" width="10" height="6"/><rect x="3" y="1" width="6" height="3"/></svg>000.000.0000</li>
      <li><svg viewBox="0 0 12 12"><path d="M0.5 2.5h11v7h-11z M0.5 2.5L6 7l5.5-4.5" stroke="#fff" stroke-width="0.8"/></svg>dana@trypairlocket.com</li>
      <li><svg viewBox="0 0 12 12"><circle cx="6" cy="6" r="5.5"/></svg>www.trypairlocket.com</li>
    </ul>

    <div class="name-band">
      <p class="name-band__name">Dana R. Whitlock, <small>MBA</small></p>
      <p class="name-band__role">Agency Principal</p>
    </div>
    <div class="band-rule"></div>
    <p class="address">Post box 0000<br>city abc road country</p>
  </section>

  <section class="card card--back">
    <svg class="badge" viewBox="0 0 120 120" role="img" aria-label="Pairlocket bottle cap emblem">
      <circle cx="60" cy="60" r="58" fill="var(--badge-ring)"/>
      <circle cx="60" cy="60" r="46" fill="var(--badge-face)"/>
      <circle cx="60" cy="60" r="36" fill="#ffffff"/>
    </svg>
    <p class="back-web">www.trypairlocket.com</p>
  </section>
</body>
</html>
```